Dentist Seminar invite please see .doc in attachments

Need an 8.5 x 11 invite designed. It will be for an invitation to attend an evening seminar on dental procedures. Feel free to utilize both front and back ONLY IF REQUIRED

See Assets & PPT with additional assets.

INSPIRATION: FIle NAME KOLVEN

Target Market(s)

Dentists

Industry/Entity Type

Dental

Other font styles liked:
• lato, garamond, palatino linotype

Colors
cee9f5
9bcb3c
0492cd
cadf82

Requirements
Must have
• Must have the colours suggested, and professional feel.
• Some of the assets merged cleanly into the design
Should not have
• Any pictures of teeth, tooth brushes or any dental product

```html
<!DOCTYPE html>
<html lang="en">
<head>
<meta charset="utf-8">
<title>CaseFlow Exchange Seminar Invitation</title>
<link href="https://fonts.googleapis.com/css2?family=Lato:wght@300;400;700;900&family=Roboto+Condensed:wght@700&display=swap" rel="stylesheet">
<style>
:root{
  --blue:#0492cd;
  --green:#9bcb3c;
  --green-soft:#cadf82;
  --ice:#cee9f5;
  --pale:#e8f1f6;
  --white:#ffffff;
  --grey:#5a5a5a;
  --screen-dark:#1c1f24;
  --page:#ece9e4;
}
*{margin:0;padding:0;box-sizing:border-box}
html,body{width:1020px;height:1200px;overflow:hidden;background:var(--page)}
body{position:relative;font-family:'Lato',sans-serif}
.card{position:absolute;left:168px;width:684px;height:528px;overflow:hidden;background:var(--blue);box-shadow:0 3px 8px rgba(0,0,0,.25)}
.card--front{top:60px}
.card--back{top:612px}
.card__shapes{position:absolute;inset:0}
.abs{position:absolute}
.title{left:25px;top:36px;font-family:'Roboto Condensed',sans-serif;font-weight:700;font-size:25px;color:var(--blue);letter-spacing:-.2px;white-space:nowrap}
.device{border-radius:12px;background:var(--screen-dark);padding:12px 10px;box-shadow:0 4px 10px rgba(0,0,0,.35)}
.device__screen{width:100%;height:100%;border-radius:2px}
.device--a{left:40px;top:83px;width:182px;height:232px}
.device--a .device__screen{background:linear-gradient(160deg,#3d4046,#8c8579 45%,#d9d9dc 75%,#f2f2f2)}
.device--b{left:217px;top:133px;width:200px;height:182px}
.device--b .device__screen{background:linear-gradient(135deg,#2a2e35,#6d7279 50%,#3a3e45)}
.callout{left:172px;top:358px;font-weight:300;font-size:20px;line-height:22px;color:var(--grey);text-align:center}
.callout-line{left:0;top:0}
.date{left:10px;top:406px;width:210px;text-align:center;color:var(--white);font-weight:700;font-size:17px;line-height:21px}
.date__icon{display:block;margin:0 auto 5px}
.tab{background:var(--green);color:var(--white);font-weight:700;clip-path:polygon(8% 0,100% 0,100% 100%,0 100%)}
.tab--synopsis{left:538px;top:48px;width:146px;height:24px;font-size:17px;line-height:24px;padding-left:28px}
.tab--objectives{left:517px;top:298px;width:167px;height:24px;font-size:13px;line-height:24px;padding-left:24px}
.synopsis{left:435px;top:84px;width:242px;font-size:8.5px;line-height:10.4px;color:var(--white);text-align:right}
.objectives{top:336px;width:152px;list-style:none;color:var(--white);font-size:8px;line-height:10.4px}
.objectives li{position:relative;padding-left:10px;margin-bottom:13px}
.objectives li::before{content:"";position:absolute;left:0;top:3px;width:4px;height:4px;border-radius:50%;background:var(--white)}
.objectives--one{left:356px}
.objectives--two{left:521px}
.band-reg{left:0;top:485px;width:270px;height:33px;background:var(--green);clip-path:polygon(0 0,88% 0,100% 100%,0 100%);font-size:15px;line-height:33px;padding-left:16px;font-weight:700;white-space:nowrap}
.band-reg__label{color:var(--blue)}
.band-reg__mail{color:var(--white);font-weight:400}
.band-phone{left:528px;top:483px;width:156px;height:35px;background:var(--green);clip-path:polygon(8% 0,100% 0,100% 100%,0 100%);color:var(--white);font-weight:700;font-size:16px;line-height:35px;padding-left:16px;display:flex;align-items:center;gap:6px}
.stamp{left:602px;top:18px;width:68px;height:66px;border:1px solid #8a8a8a;background:var(--white)}
.thumb{width:125px;height:95px;border-radius:7px;background:var(--screen-dark);padding:8px 7px;box-shadow:0 3px 8px rgba(0,0,0,.35)}
.thumb__screen{width:100%;height:100%}
.thumb--1{left:27px;top:78px}.thumb--1 .thumb__screen{background:linear-gradient(180deg,#3b3b3b,#b7585a 55%,#e8e0d8)}
.thumb--2{left:175px;top:78px}.thumb--2 .thumb__screen{background:linear-gradient(180deg,#2c3a2e,#7b3f8a 55%,#e6e0c8)}
.thumb--3{left:27px;top:190px}.thumb--3 .thumb__screen{background:linear-gradient(180deg,#2e2e2e,#bcbcbc 55%,#efefef)}
.thumb--4{left:175px;top:190px}.thumb--4 .thumb__screen{background:linear-gradient(135deg,#2e2e2e,#9a9a9a 55%,#5a7fd0)}
.tab--bio{left:0;top:310px;width:140px;height:24px;font-size:16px;line-height:24px;padding-left:22px;clip-path:polygon(0 0,100% 0,88% 100%,0 100%)}
.bio{left:19px;top:352px;width:350px;font-size:8.3px;line-height:10.5px;color:var(--white)}
.btn-reg{left:115px;top:445px;width:150px;height:27px;border-radius:5px;background:var(--green);color:var(--white);font-weight:700;font-size:16px;line-height:27px;text-align:center}
.contact-lines{left:0;top:0}
.contact{top:488px;color:var(--white);font-size:19px;font-weight:400;white-space:nowrap}
.contact--mail{left:19px}
.contact--phone{left:225px;font-weight:700}
.venue{left:527px;top:471px;color:var(--white);font-size:12px;line-height:14px}
.venue strong{font-weight:700}
</style>
</head>
<body>

<section class="card card--front">
  <svg class="card__shapes" viewBox="0 0 684 528" width="684" height="528" aria-hidden="true">
    <polygon points="372,0 525,0 352,430 312,410" fill="var(--green)"/>
    <polygon points="366,0 420,0 330,470 300,455" fill="var(--pale)"/>
    <polygon points="0,0 380,0 318,448 0,350" fill="var(--white)"/>
  </svg>

  <h1 class="abs title">CaseFlow Exchange™ : Impressions</h1>

  <div class="abs device device--a"><div class="device__screen" role="img" aria-label="Tablet screenshot of planning software showing a 3D jaw model with implants"></div></div>
  <div class="abs device device--b"><div class="device__screen" role="img" aria-label="Tablet screenshot of planning software showing CT scan views"></div></div>

  <svg class="abs callout-line" width="684" height="528" aria-hidden="true">
    <polyline points="324,300 324,368 298,368" fill="none" stroke="#777" stroke-width="1"/>
  </svg>
  <p class="abs callout">PlanVista<br>Presenter</p>

  <div class="abs date">
    <svg class="date__icon" width="26" height="26" viewBox="0 0 26 26" aria-hidden="true">
      <circle cx="13" cy="13" r="12" fill="none" stroke="#fff" stroke-width="1.5"/>
      <rect x="7" y="8" width="12" height="10" rx="1" fill="none" stroke="#fff" stroke-width="1.3"/>
      <line x1="7" y1="11" x2="19" y2="11" stroke="#fff" stroke-width="1.3"/>
      <line x1="10" y1="6.5" x2="10" y2="9" stroke="#fff" stroke-width="1.3"/>
      <line x1="16" y1="6.5" x2="16" y2="9" stroke="#fff" stroke-width="1.3"/>
    </svg>
    November 13, 2017<br>6:30 – 9:30pm
  </div>

  <div class="abs band-reg"><span class="band-reg__label">Registration:</span><span class="band-reg__mail">rsvp.dr@email.com</span></div>

  <h2 class="abs tab tab--synopsis">Synopsis:</h2>
  <p class="abs synopsis">This presentation will cover the recent advances in digital technology and its use in dentistry. Digital protocols will be introduced that can improve upon traditional treatment planning approaches. The use of modern 3D technology and the digital workflow can simplify advanced procedures enhancing the predictability of the surgical outcomes. Through the use of state of the art diagnostic imaging technologies, intra-oral scanning, live guided navigation, and 3D printing; multiple digital workflows and their surgical applications will be discussed through real clinical cases from Dr Harlow's surgical practice. This groundbreaking lecture will showcase the synergy between advanced technology and fundamental biological principles to revolutionize the modern practice of periodontics and implantology. Multiple innovative protocols to treat advanced surgical cases will be presented with techniques that have never been seen before.</p>

  <h2 class="abs tab tab--objectives">Learning Objectives:</h2>
  <ul class="abs objectives objectives--one">
    <li>Discuss the use of modern digital technologies like CBCT, intra-oral scanning, and 3D printing.</li>
    <li>Learn to digitally plan surgical procedures and use 3D printed surgical guides</li>
    <li>Understand the benefits of microsurgery and the use of surgical operating microscope</li>
    <li>Understand the benefits of digital technology in surgical treatment planning</li>
  </ul>
  <ul class="abs objectives objectives--two">
    <li>Understanding and benefits of live guided navigation surgery and its applications</li>
    <li>Understand how computer automated design software can improve upon real live surgery.</li>
    <li>Learn about innovative procedures like digitally guided bone block harvesting, digitally created bone grafts, and osteotomy guides.</li>
  </ul>

  <div class="abs band-phone">
    <svg width="18" height="18" viewBox="0 0 18 18" aria-hidden="true">
      <circle cx="9" cy="9" r="8" fill="none" stroke="#fff" stroke-width="1.3"/>
      <path d="M6 5.2c.5-.4 1-.3 1.2.1l.7 1.4c.2.4 0 .7-.3 1l-.4.3c.4 1 1.2 1.8 2.2 2.2l.3-.4c.3-.3.6-.5 1-.3l1.4.7c.4.2.5.7.1 1.2-.6.7-1.4 1-2.3.7-2-.7-3.6-2.3-4.3-4.3-.3-.9 0-1.7.4-2.6z" fill="#fff"/>
    </svg>
    555-014-2290
  </div>
</section>

<section class="card card--back">
  <svg class="card__shapes" viewBox="0 0 684 528" width="684" height="528" aria-hidden="true">
    <polygon points="285,0 684,0 684,370 420,445" fill="var(--green)"/>
    <polygon points="312,10 684,0 684,378 452,450" fill="var(--pale)"/>
    <polygon points="335,22 684,10 684,386 468,452" fill="var(--white)"/>
  </svg>

  <div class="abs stamp" aria-hidden="true"></div>

  <div class="abs thumb thumb--1"><div class="thumb__screen" role="img" aria-label="Tablet screenshot of an implant placement clinical view"></div></div>
  <div class="abs thumb thumb--2"><div class="thumb__screen" role="img" aria-label="Tablet screenshot of a digital guide design"></div></div>
  <div class="abs thumb thumb--3"><div class="thumb__screen" role="img" aria-label="Tablet screenshot of a 3D skull scan"></div></div>
  <div class="abs thumb thumb--4"><div class="thumb__screen" role="img" aria-label="Tablet screenshot of a jaw model with planned implants"></div></div>

  <h2 class="abs tab tab--bio">Biography</h2>
  <p class="abs bio">Lorem Ipsum is simply dummy text of the printing and typesetting industry. Lorem Ipsum has been the industry's standard dummy text ever since the 1500s, when an unknown printer took a galley of type and scrambled it to make a type specimen book. It has survived not only five centuries, but also the leap into electronic typesetting, remaining essentially unchanged. It was popularised in the 1960s with the release of Letraset sheets containing Lorem Ipsum passages, and more recently with desktop publishing software like Aldus PageMaker including versions of</p>

  <div class="abs btn-reg">Registration Now</div>

  <svg class="abs contact-lines" width="684" height="528" aria-hidden="true">
    <polyline points="115,459 87,459 87,470" fill="none" stroke="#fff" stroke-width="1"/>
    <polyline points="265,459 295,459 295,470" fill="none" stroke="#fff" stroke-width="1"/>
    <circle cx="87" cy="478" r="8" fill="none" stroke="#fff" stroke-width="1.2"/>
    <rect x="82.5" y="474.5" width="9" height="6.5" fill="none" stroke="#fff" stroke-width="1"/>
    <polyline points="82.5,474.5 87,478.5 91.5,474.5" fill="none" stroke="#fff" stroke-width="1"/>
    <circle cx="295" cy="478" r="8" fill="none" stroke="#fff" stroke-width="1.2"/>
    <path d="M292 474.2c.4-.3.8-.2 1 .1l.5 1c.1.3 0 .5-.2.7l-.3.2c.3.7.9 1.3 1.6 1.6l.2-.3c.2-.2.4-.3.7-.2l1 .5c.3.1.4.5.1.9-.4.5-1 .7-1.6.5-1.5-.5-2.6-1.6-3.1-3.1-.2-.6 0-1.2.3-1.8z" fill="#fff"/>
    <path d="M508 474a6 6 0 0 1 12 0c0 4.5-6 10-6 10s-6-5.5-6-10z" fill="none" stroke="#fff" stroke-width="1.4"/>
    <circle cx="514" cy="474" r="2" fill="#fff"/>
  </svg>
  <p class="abs contact contact--mail">rsvp.dr@email.com</p>
  <p class="abs contact contact--phone">555-014-2290</p>

  <p class="abs venue"><strong>Maple Grove Banquet Hall</strong><br>48 Fernlea Ave. Lakeview,<br>Ontario, A1B 2C3</p>
</section>

</body>
</html>
```